Can you create a Business Card based on the Logo you designed.

See example and would like to see other examples.

Trying to keep it very clean with a focus on the logo and name.

```html
<!DOCTYPE html>
<html lang="en">
<head>
<meta charset="utf-8">
<title>Fieldrow Business Card</title>
<link href="https://fonts.googleapis.com/css2?family=Montserrat:wght@600;700&family=Open+Sans:wght@400;600&display=swap" rel="stylesheet">
<style>
  :root {
    --bg: #dcdcdc;
    --card-white: #f6f6f6;
    --brand-green: #1f7a3a;
    --leaf-green: #7ab541;
    --accent-orange: #e9963a;
    --ink: #2b2b2b;
    --rule: #3a3a3a;
    --white: #ffffff;
  }
  * { box-sizing: border-box; margin: 0; padding: 0; }
  html, body {
    width: 1200px;
    height: 800px;
    overflow: hidden;
    background: var(--bg);
  }
  .canvas {
    position: relative;
    width: 1200px;
    height: 800px;
  }
  .card {
    position: absolute;
    border-radius: 28px;
    box-shadow: 0 10px 30px rgba(0,0,0,0.15);
  }
  /* Front: vertical white card */
  .card-front {
    left: 110px;
    top: 100px;
    width: 360px;
    height: 600px;
    background: var(--card-white);
    padding: 70px 48px 60px;
    display: flex;
    flex-direction: column;
  }
  .front-brand {
    display: flex;
    align-items: center;
    justify-content: center;
    gap: 10px;
    margin-top: 20px;
  }
  .front-brand .brand-dot {
    width: 18px;
    height: 18px;
    border-radius: 50%;
    background: var(--accent-orange);
  }
  .front-brand .brand-name {
    font-family: "Montserrat", sans-serif;
    font-weight: 700;
    font-size: 46px;
    color: var(--brand-green);
    letter-spacing: -0.5px;
  }
  .person {
    margin-top: 90px;
  }
  .person-name {
    font-family: "Montserrat", sans-serif;
    font-weight: 700;
    font-size: 26px;
    color: var(--brand-green);
  }
  .person-title {
    font-family: "Open Sans", sans-serif;
    font-size: 17px;
    color: var(--accent-orange);
    margin-top: 2px;
  }
  .divider {
    width: 64px;
    height: 1px;
    background: var(--rule);
    margin: 40px 0 40px;
  }
  .contact-list {
    list-style: none;
    display: flex;
    flex-direction: column;
    gap: 8px;
  }
  .contact-item {
    display: flex;
    align-items: center;
    gap: 10px;
    font-family: "Open Sans", sans-serif;
    font-size: 16px;
    color: var(--ink);
  }
  .contact-icon {
    width: 14px;
    height: 14px;
    flex: none;
  }
  /* Back: horizontal green card */
  .card-back {
    left: 530px;
    top: 220px;
    width: 600px;
    height: 360px;
    background: var(--leaf-green);
    display: flex;
    flex-direction: column;
    align-items: center;
    justify-content: center;
    gap: 34px;
  }
  .back-brand {
    display: flex;
    align-items: center;
    gap: 16px;
  }
  .back-brand .brand-dot {
    width: 30px;
    height: 30px;
    border-radius: 50%;
    background: var(--white);
  }
  .back-brand .brand-name {
    font-family: "Montserrat", sans-serif;
    font-weight: 700;
    font-size: 82px;
    color: var(--white);
    letter-spacing: -1px;
  }
  .back-url {
    font-family: "Open Sans", sans-serif;
    font-size: 18px;
    color: var(--white);
    letter-spacing: 5px;
  }
</style>
</head>
<body>
<main class="canvas">
  <section class="card card-front">
    <div class="front-brand">
      <span class="brand-dot"></span>
      <span class="brand-name">Fieldrow</span>
    </div>
    <div class="person">
      <h1 class="person-name">Marcus Hale</h1>
      <p class="person-title">Chief Executive officer</p>
    </div>
    <div class="divider"></div>
    <ul class="contact-list">
      <li class="contact-item">
        <svg class="contact-icon" viewBox="0 0 16 16" aria-hidden="true"><path fill="#1f7a3a" d="M3.5 1.5l2.5 0 1 3.5-1.6 1.2a8 8 0 0 0 4.4 4.4L11 9l3.5 1v2.5c0 .8-.7 1.5-1.5 1.5C7 14 2 9 2 3c0-.8.7-1.5 1.5-1.5z"/></svg>
        <span>+1 (555) 014-2287</span>
      </li>
      <li class="contact-item">
        <svg class="contact-icon" viewBox="0 0 16 16" aria-hidden="true"><rect x="1" y="3" width="14" height="10" rx="1" fill="#1f7a3a"/><polyline points="1.5,4 8,9 14.5,4" fill="none" stroke="#f6f6f6" stroke-width="1.4"/></svg>
        <span>ceo@fieldrow.com</span>
      </li>
      <li class="contact-item">
        <svg class="contact-icon" viewBox="0 0 16 16" aria-hidden="true"><circle cx="8" cy="8" r="7" fill="#1f7a3a"/><path d="M1 8h14M8 1c-3 3.5-3 10.5 0 14M8 1c3 3.5 3 10.5 0 14" fill="none" stroke="#f6f6f6" stroke-width="1"/></svg>
        <span>www.fieldrow.com</span>
      </li>
    </ul>
  </section>

  <section class="card card-back">
    <div class="back-brand">
      <span class="brand-dot"></span>
      <span class="brand-name">Fieldrow</span>
    </div>
    <p class="back-url">www.fieldrow.com</p>
  </section>
</main>
</body>
</html>
```